Business Card for TQB Field Services

Would like a large logo on one side. On the other side, logo on one side and company phone number, address, and email on the other side. I don't have a logo so please create one for us.
Updates
I don't have a logo, so please create one for us.
Target Market(s)
TQB Field Services
Industry/Entity Type
Surveyor
Contact Information for Business Card
Would like a large logo on one side. On the other side, logo on one side and company phone number, address, and email on the other side
Requirements
Nice to have
- would like the initials to be incorporated with the logo

```html
<!DOCTYPE html>
<html lang="en">
<head>
<meta charset="utf-8">
<title>TQB Field Services – Business Card</title>
<link rel="stylesheet" href="https://fonts.googleapis.com/css2?family=Michroma&family=Open+Sans:wght@400;700&display=swap">
<style>
  :root {
    --page: #2a292b;
    --card-dark: #2b2a2c;
    --card-white: #ffffff;
    --plan-tone: #f1f1f2;
    --red: #e1262b;
    --red-deep: #9e1419;
    --fold-grey: #8d8e90;
    --ink: #1d1d1f;
    --logo-grey: #6d6e71;
    --muted: #8a8a8c;
    --contact: #f2f2f2;
  }
  * { box-sizing: border-box; margin: 0; padding: 0; }
  html, body { width: 1200px; height: 800px; overflow: hidden; }
  body {
    background: var(--page);
    font-family: "Open Sans", Arial, sans-serif;
    position: relative;
  }
  .card {
    position: absolute;
    width: 540px;
    height: 309px;
    top: 246px;
    overflow: hidden;
    background: var(--card-white);
    box-shadow: 0 14px 30px rgba(0,0,0,.45);
  }
  .card--front { left: 40px; }
  .card--back { left: 620px; }
  .card__shapes { position: absolute; inset: 0; width: 100%; height: 100%; }

  .brand {
    position: absolute;
    display: flex;
    align-items: center;
    gap: 8px;
    color: var(--logo-grey);
    font-weight: 700;
    white-space: nowrap;
  }
  .brand__dot { border-radius: 50%; background: var(--red); flex: none; }
  .card--front .brand { left: 34px; top: 92px; font-size: 17px; }
  .card--front .brand__dot { width: 14px; height: 14px; }

  .holder { position: absolute; left: 34px; bottom: 44px; }
  .holder__name {
    font-family: "Michroma", "Open Sans", sans-serif;
    font-size: 15px;
    color: var(--ink);
    letter-spacing: .5px;
  }
  .holder__role { font-size: 12px; color: var(--muted); margin-top: 4px; }

  .contact-list {
    position: absolute;
    left: 372px;
    top: 58px;
    list-style: none;
    color: var(--contact);
    font-size: 10.5px;
  }
  .contact-list li { display: flex; align-items: center; gap: 8px; height: 20px; white-space: nowrap; }
  .contact-list svg { width: 13px; height: 13px; flex: none; }
  .contact-list .indent { padding-left: 21px; }

  .card--back .brand {
    left: 110px; top: 122px; font-size: 30px;
  }
  .card--back .brand__dot { width: 26px; height: 26px; }
</style>
</head>
<body>

<section class="card card--front" aria-label="Card front">
  <svg class="card__shapes" viewBox="0 0 540 309" preserveAspectRatio="none">
    <polygon points="330,0 540,0 540,309 420,309 445,212 362,192" fill="var(--card-dark)"/>
    <polygon points="305,0 332,0 364,194 298,138" fill="var(--red)"/>
    <polygon points="364,194 445,212 425,238" fill="var(--fold-grey)"/>
    <polygon points="425,238 447,212 440,309 418,309" fill="var(--red-deep)"/>
  </svg>
  <div class="brand"><span class="brand__dot"></span>TQB Field Services</div>
  <div class="holder">
    <p class="holder__name">MAREN OLSBY</p>
    <p class="holder__role">Designation</p>
  </div>
  <ul class="contact-list">
    <li><svg viewBox="0 0 16 16"><circle cx="8" cy="8" r="7" fill="none" stroke="currentColor"/><path d="M5.5 4.5l1.5 0 .7 2-1 .8a5 5 0 0 0 2 2l.8-1 2 .7v1.5c-3 .5-6.5-3-6-6z" fill="currentColor"/></svg>+64 555 018 274</li>
    <li><svg viewBox="0 0 16 16"><circle cx="8" cy="8" r="7" fill="none" stroke="currentColor"/><rect x="4.5" y="5.5" width="7" height="5" fill="none" stroke="currentColor"/><path d="M4.5 5.5L8 8.3l3.5-2.8" fill="none" stroke="currentColor"/></svg>office@tqbfield.example</li>
    <li><svg viewBox="0 0 16 16"><circle cx="8" cy="8" r="7" fill="none" stroke="currentColor"/><circle cx="8" cy="8" r="3.5" fill="none" stroke="currentColor"/><path d="M4.5 8h7M8 4.5v7" stroke="currentColor"/></svg>www.tqbfield.example</li>
    <li><svg viewBox="0 0 16 16"><circle cx="8" cy="8" r="7" fill="none" stroke="currentColor"/><circle cx="8" cy="8" r="2" fill="currentColor"/></svg>profile.tqbfield.example</li>
    <li><svg viewBox="0 0 16 16"><circle cx="8" cy="8" r="7" fill="none" stroke="currentColor"/><path d="M8 12s-3-3-3-5a3 3 0 0 1 6 0c0 2-3 5-3 5z" fill="currentColor"/></svg>PO Box 000 Ferndale NS</li>
    <li class="indent">Kestrel Bay 7316</li>
  </ul>
</section>

<section class="card card--back" aria-label="Card back">
  <svg class="card__shapes" viewBox="0 0 540 309" preserveAspectRatio="none">
    <rect x="0" y="0" width="540" height="309" fill="var(--plan-tone)" role="img" aria-label="Faint architectural floor plan backdrop"/>
    <polygon points="540,40 540,309 150,309 196,258 345,222 420,196 470,150" fill="var(--card-dark)"/>
    <polygon points="500,38 520,20 470,150 448,170" fill="var(--red)"/>
    <polygon points="470,150 448,170 420,196 452,186" fill="var(--fold-grey)"/>
    <polygon points="345,222 372,206 365,270 330,280" fill="var(--red-deep)"/>
    <polygon points="196,258 345,222 330,280 180,300" fill="var(--fold-grey)" opacity=".55"/>
  </svg>
  <div class="brand"><span class="brand__dot"></span>TQB Field Services</div>
</section>

</body>
</html>
```